business cards

we want our logos on the back
the information on it are on the design I've uploaded
come up with whatever you think is best, we want something professional, sophisticated and sleek.

```html
<!DOCTYPE html>
<html lang="en">
<head>
<meta charset="utf-8">
<title>Vantage business cards</title>
<link rel="stylesheet" href="https://fonts.googleapis.com/css2?family=Montserrat:wght@300;400;600&display=swap">
<style>
:root{
  --stage:#1d1f22;
  --card:#0b0b0b;
  --green:#5cb946;
  --white:#f2f2f2;
}
*{margin:0;padding:0;box-sizing:border-box}
html,body{width:1200px;height:2512px;overflow:hidden;background:var(--stage)}
body{position:relative;font-family:"Montserrat",sans-serif;color:var(--white)}
.card{position:absolute;background:var(--card);border-radius:54px;box-shadow:0 14px 40px rgba(0,0,0,.55)}
.card--one{left:104px;top:173px;width:992px;height:594px}
.card--two{left:104px;top:851px;width:992px;height:592px}
.card--three{left:88px;top:1757px;width:1024px;height:583px}
.brand{position:absolute;transform:translate(-50%,-50%);display:flex;align-items:center;gap:16px;white-space:nowrap}
.brand__dot{width:18px;height:18px;border-radius:50%;background:var(--green);flex:none}
.brand__name{font-weight:300;font-size:46px;line-height:1;letter-spacing:12px;margin-right:-12px;color:var(--white)}
.divider{position:absolute;width:2px;background:var(--green)}
.info{position:absolute;font-weight:300;font-size:23px;line-height:33px;letter-spacing:.3px}
.info__name{font-weight:600;font-size:38px;line-height:44px;color:var(--green);margin-bottom:2px;letter-spacing:0}
.info__address{margin-top:10px}
.contacts{margin-top:14px;list-style:none}
.contacts li{display:flex;align-items:center;gap:12px;height:33px}
.contacts .contacts__email{font-size:17px}
.icon{width:20px;height:20px;flex:none}
</style>
</head>
<body>
<svg width="0" height="0" style="position:absolute">
  <defs>
    <symbol id="icon-phone" viewBox="0 0 20 20"><circle cx="10" cy="10" r="10" fill="#5cb946"/><path d="M7 5.2c.4-.3.9-.2 1.1.2l.9 1.7c.2.4.1.8-.2 1.1l-.6.5c.5 1.1 1.3 1.9 2.3 2.4l.5-.6c.3-.3.7-.4 1.1-.2l1.7.9c.4.2.5.7.2 1.1l-.7.9c-.4.5-1.1.7-1.7.5-2.6-.9-4.5-2.9-5.4-5.4-.2-.6 0-1.3.5-1.7z" fill="#0b0b0b"/></symbol>
    <symbol id="icon-fax" viewBox="0 0 20 20"><circle cx="10" cy="10" r="10" fill="#5cb946"/><rect x="7" y="5" width="6" height="3" fill="#0b0b0b"/><rect x="5" y="8.5" width="10" height="5" rx="1" fill="#0b0b0b"/><rect x="7" y="12" width="6" height="3.5" fill="#0b0b0b"/></symbol>
    <symbol id="icon-mail" viewBox="0 0 20 20"><circle cx="10" cy="10" r="10" fill="#5cb946"/><rect x="5" y="6.5" width="10" height="7" rx="1" fill="#0b0b0b"/><path d="M5.5 7l4.5 3.6L14.5 7" fill="none" stroke="#5cb946" stroke-width="1"/></symbol>
  </defs>
</svg>

<section class="card card--one">
  <div class="brand" style="left:250px;top:296px"><span class="brand__dot"></span><span class="brand__name">VANTAGE</span></div>
  <div class="divider" style="left:469px;top:131px;height:329px"></div>
  <div class="info" style="left:501px;top:116px">
    <p class="info__name">Daniel Whitford</p>
    <p>DIRECTOR</p>
    <p>SENIOR PHYSIOTHERAPIST</p>
    <p>BHlthSSc, MPhysioprac, MExSc(S&amp;C)</p>
    <p>ASCA Level 2</p>
    <p class="info__address">17 Carrow Rd, Kingsley Park</p>
    <ul class="contacts">
      <li><svg class="icon"><use href="#icon-phone"/></svg>03 5550 1184</li>
      <li><svg class="icon"><use href="#icon-fax"/></svg>03 5550 2291</li>
      <li class="contacts__email"><svg class="icon"><use href="#icon-mail"/></svg>daniel@vantagehealthclinic.com.au</li>
    </ul>
  </div>
</section>

<section class="card card--two">
  <div class="brand" style="left:277px;top:296px"><span class="brand__dot"></span><span class="brand__name">VANTAGE</span></div>
  <div class="divider" style="left:507px;top:129px;height:328px"></div>
  <div class="info" style="left:548px;top:118px">
    <p class="info__name">Marco Leventis</p>
    <p>DIRECTOR -</p>
    <p>PERSONAL TRAINER</p>
    <p>SPORTS NUTRITIONIST</p>
    <p>BEcSc</p>
    <p class="info__address">17 Carrow Rd, Kingsley Park</p>
    <ul class="contacts">
      <li><svg class="icon"><use href="#icon-phone"/></svg>03 5550 1184</li>
      <li><svg class="icon"><use href="#icon-fax"/></svg>03 5550 2291</li>
      <li class="contacts__email"><svg class="icon"><use href="#icon-mail"/></svg>info@vantagehealthclinic.com.au</li>
    </ul>
  </div>
</section>

<section class="card card--three">
  <div class="brand" style="left:235px;top:293px"><span class="brand__dot"></span><span class="brand__name">VANTAGE</span></div>
  <div class="divider" style="left:487px;top:127px;height:327px"></div>
  <div class="info" style="left:535px;top:114px">
    <p class="info__name">Oliver Hastings</p>
    <p>DIRECTOR</p>
    <p>SENIOR PHYSIOTHERAPIST</p>
    <p>BHlthSSc, MPhysioprac, MExSc(S&amp;C)</p>
    <p>ASCA Level 2</p>
    <p class="info__address">17 Carrow Rd, Kingsley Park</p>
    <ul class="contacts">
      <li><svg class="icon"><use href="#icon-phone"/></svg>03 5550 1184</li>
      <li><svg class="icon"><use href="#icon-fax"/></svg>03 5550 2291</li>
      <li class="contacts__email"><svg class="icon"><use href="#icon-mail"/></svg>oliver@vantagehealthclinic.com.au</li>
    </ul>
  </div>
</section>
</body>
</html>
```